KTR Engineering Pty Ltd

I have already had Corvale welding and fabrication cards made , my business has changed too KTR engineering Pty Ltd so I need my logo changed on the cards
one side have my logo then the other side have what we do.
front side logo and details
owner /operator : Lachlan Meravic
email: ktr.works@ironvalemail.com
number: 0491537204
ABN: 47 261 538 902
ACN: 718 352 946
on back have in dot points what we do:
* structural steel erection
* precast panels
* site welding
*steel alteration & repair
* rigging & dogging
*labour hire
all details in breif

```html
<!DOCTYPE html>
<html lang="en">
<head>
<meta charset="utf-8">
<title>KTR Engineering Pty Ltd – Business Cards</title>
<link href="https://fonts.googleapis.com/css2?family=Open+Sans:wght@400;600;800&family=Montserrat:wght@700&display=swap" rel="stylesheet">
<style>
  :root{
    --navy:#1c2840;
    --navy-deep:#162036;
    --rust:#a5443a;
    --white:#ffffff;
    --ink:#1c2840;
    --stage:#e6e7ea;
  }
  html,body{margin:0;padding:0;overflow:hidden;}
  body{width:1200px;height:913px;background:var(--stage);position:relative;font-family:"Open Sans",sans-serif;}
  .card{position:absolute;width:560px;height:320px;border-radius:18px;overflow:hidden;box-shadow:0 10px 26px rgba(0,0,0,.18);}

  /* brand block: mark beside a stacked name + phone */
  .brand{position:absolute;display:flex;align-items:flex-start;gap:10px;}
  .brand__mark{width:16px;height:16px;background:var(--rust);flex:none;margin-top:30px;}
  .brand__stack{display:flex;flex-direction:column;}
  .brand__name{font-weight:800;font-size:22px;line-height:1.1;letter-spacing:.5px;text-transform:uppercase;}
  .brand__phone{margin-top:8px;font-weight:600;font-size:12px;line-height:1;color:var(--rust);letter-spacing:1px;}

  /* back card */
  .card--services{left:60px;top:90px;background:linear-gradient(135deg,#22304b 0%,var(--navy-deep) 100%);}
  .card--services .brand{left:40px;top:115px;}
  .card--services .brand__name{color:var(--white);width:200px;}
  .services{position:absolute;left:300px;top:70px;margin:0;padding:0;list-style:none;color:var(--white);font-size:16px;line-height:27px;}
  .services li{position:relative;padding-left:16px;}
  .services li::before{content:"";position:absolute;left:0;top:12px;width:6px;height:6px;border-radius:50%;background:var(--rust);}

  /* front card */
  .card--contact{left:580px;top:500px;background:var(--white);}
  .card--contact svg.wave{position:absolute;left:0;top:0;}
  .tab{position:absolute;right:-8px;top:26px;width:22px;height:34px;border-radius:11px;background:var(--rust);}
  .card--contact .brand{left:36px;top:88px;}
  .card--contact .brand__name{color:var(--ink);width:220px;font-size:24px;}
  .person{position:absolute;right:40px;top:22px;text-align:right;}
  .person__name{font-family:"Montserrat",sans-serif;font-weight:700;font-size:22px;line-height:28px;color:var(--ink);margin:0;}
  .person__role{font-size:15px;line-height:20px;color:var(--rust);margin:2px 0 0;}
  .details{position:absolute;right:28px;top:160px;text-align:right;color:var(--white);font-size:13px;line-height:22px;}
  .details p{margin:0;display:flex;justify-content:flex-end;align-items:center;gap:6px;white-space:nowrap;}
  .details svg{flex:none;}
</style>
</head>
<body>

<section class="card card--services" aria-label="Back of card">
  <div class="brand">
    <span class="brand__mark"></span>
    <div class="brand__stack">
      <span class="brand__name">KTR Engineering Pty Ltd</span>
      <span class="brand__phone">0491537204</span>
    </div>
  </div>
  <ul class="services">
    <li>structural steel erection</li>
    <li>precast panels</li>
    <li>site welding</li>
    <li>steel alteration &amp; repair</li>
    <li>rigging &amp; dogging</li>
    <li>labour hire</li>
  </ul>
</section>

<section class="card card--contact" aria-label="Front of card">
  <svg class="wave" width="560" height="320" viewBox="0 0 560 320">
    <path d="M560 108 C430 94 350 128 300 206 C262 266 220 286 0 288 L0 320 L560 320 Z" fill="var(--navy)"/>
    <path d="M560 96 C428 82 340 118 288 198 C250 258 210 276 0 278" fill="none" stroke="var(--navy)" stroke-width="4"/>
    <path d="M540 86 C420 74 330 108 276 190 C238 250 198 268 0 268" fill="none" stroke="var(--rust)" stroke-width="4"/>
    <path d="M0 300 L250 300" stroke="var(--white)" stroke-width="2"/>
  </svg>
  <span class="tab"></span>
  <div class="person">
    <p class="person__name">Lachlan Meravic</p>
    <p class="person__role">owner / operator</p>
  </div>
  <div class="brand">
    <span class="brand__mark"></span>
    <div class="brand__stack">
      <span class="brand__name">KTR Engineering Pty Ltd</span>
      <span class="brand__phone">0491537204</span>
    </div>
  </div>
  <div class="details">
    <p>0491537204
      <svg width="12" height="12" viewBox="0 0 24 24"><path fill="var(--rust)" d="M6.6 10.8a15 15 0 0 0 6.6 6.6l2.2-2.2c.3-.3.7-.4 1-.2 1.1.4 2.3.6 3.6.6.6 0 1 .4 1 1V20c0 .6-.4 1-1 1A17 17 0 0 1 3 4c0-.6.4-1 1-1h3.5c.6 0 1 .4 1 1 0 1.3.2 2.5.6 3.6.1.3 0 .7-.2 1z"/></svg>
    </p>
    <p>ktr.works@ironvalemail.com
      <svg width="12" height="10" viewBox="0 0 24 18"><path fill="var(--rust)" d="M0 0h24v18H0z"/><path fill="none" stroke="var(--navy)" stroke-width="2" d="M1 1l11 9 11-9"/></svg>
    </p>
    <p>ABN: 47 261 538 902</p>
    <p>ACN: 718 352 946</p>
  </div>
</section>

</body>
</html>
```